Looking to develop game card. It will be included in Dozen Golf Balls Using the TorBLIVVO THEME ( 6 new games) and (6 old games) Attached is a picture of a three fold score card. Six games on the front layout and six on the back. Sample is "name of game and rules" Be creative in the set up. should be easy to read and simple to follow.

```html
<!DOCTYPE html>
<html lang="en">
<head>
<meta charset="utf-8">
<title>TorBLIVVO Game Card</title>
<link href="https://fonts.googleapis.com/css2?family=Fira+Sans:ital,wght@0,400;0,600;0,700;0,800;1,400;1,700;1,800&display=swap" rel="stylesheet">
<style>
:root{
  --red:#d7141a;
  --green:#2e7d3a;
  --green-light:#8cc58a;
  --blue:#22468a;
  --navy:#264a86;
  --ink:#111;
  --white:#fff;
  --paper:#f6f6f6;
  --frame:#5a5a5a;
  --steel-1:#9a9a9a;
  --steel-2:#d9d9d9;
  --steel-3:#6e6e6e;
}
*{box-sizing:border-box;margin:0;padding:0}
html,body{width:1200px;height:617px;overflow:hidden}
body{
  font-family:"Fira Sans",Arial,sans-serif;
  color:var(--ink);
  background:linear-gradient(180deg,var(--steel-3) 0%,var(--steel-1) 25%,var(--steel-2) 50%,var(--steel-1) 75%,var(--steel-3) 100%);
  position:relative;
}
.panel{position:absolute;border-radius:9px;overflow:hidden;border:3px solid var(--frame)}
.panel--light{background:var(--paper)}
.panel--dark{background:linear-gradient(160deg,#000 0%,#0d0d0d 45%,#5c5c5c 75%,#111 100%);color:var(--white)}
.panel--roulette{left:30px;top:28px;width:368px;height:276px;border-color:var(--red)}
.panel--horsemen{left:415px;top:28px;width:371px;height:280px;border-color:var(--blue)}
.panel--ball{left:801px;top:28px;width:370px;height:292px}
.panel--calling{left:30px;top:347px;width:368px;height:243px;border-color:var(--green)}
.panel--insurance{left:415px;top:347px;width:371px;height:243px}
.panel--bachelor{left:801px;top:347px;width:370px;height:243px}

.title{position:absolute;left:9px;top:5px;font-weight:700;font-size:29px;white-space:nowrap;letter-spacing:.2px}
.title .num{font-size:42px;font-weight:800;margin-right:7px;vertical-align:-4px}
.title sup{font-size:11px;font-weight:600;vertical-align:14px}
.title--tight{font-size:27px}
.num--red{color:var(--red)} .num--green{color:var(--green)} .num--blue{color:var(--blue)} .num--white{color:var(--white)}
.accent-red{color:var(--red)}
.tagline{position:absolute;left:0;right:0;text-align:center;font-style:italic;font-size:14px}

.rules{position:absolute;left:12px;right:12px;list-style:none;font-size:9.5px;line-height:1.3}
.rules li{display:flex;align-items:flex-start;gap:12px;margin-bottom:10px}
.badge{flex:none;width:15px;height:15px;border-radius:50%;font-size:9px;font-weight:700;display:flex;align-items:center;justify-content:center;color:var(--white);margin-left:4px}
.badge--red{background:var(--red)} .badge--green{background:var(--green)} .badge--light{background:var(--white);color:var(--ink)}
.rules b{font-weight:700}

.win{position:absolute;left:0;right:0;top:182px;text-align:center;font-size:8px}
.cards{position:absolute;left:38px;top:200px;display:flex;gap:15px}
.mini-card{width:62px;height:68px;border-radius:2px}
.mini-card--curl{background:linear-gradient(#c3242b,#8e1419)}
.mini-card--side{background:linear-gradient(#2e8a43,#1c5e2a)}
.mini-card--snap{background:linear-gradient(#2b5bb0,#173c80)}
.mini-card--chucka{background:linear-gradient(#111,#2b3b2b)}

.horsemen-art{position:absolute;left:90px;top:40px;width:200px;height:170px;background:radial-gradient(ellipse at center,rgba(120,120,120,.28),rgba(120,120,120,0) 70%)}
.tally{position:absolute;left:14px;right:30px;top:84px;list-style:none}
.tally li{display:flex;align-items:center;height:24.5px}
.tally .tick{width:15px;height:15px;margin-right:9px;flex:none}
.tally .name{font-style:italic;font-weight:800;font-size:20px;flex:1}
.tally .name sup{font-size:9px;vertical-align:9px}
.tally .pts{font-style:italic;font-weight:800;font-size:15px}
.name--red{color:var(--red)} .name--green{color:var(--green)} .name--blue{color:var(--blue)}
.sum{position:absolute;left:0;right:0;top:196px;text-align:center;font-style:italic;font-size:13px}
.grand{position:absolute;left:37px;right:39px;top:221px;height:52px;border-radius:6px;background:var(--navy);color:var(--white);display:flex;align-items:center;gap:14px;padding-left:16px}
.grand svg{flex:none}
.grand h3{font-size:12.5px;font-weight:700}
.grand p{font-size:10.5px;line-height:1.25}

.ball-art{position:absolute;right:0;bottom:0;width:260px;height:150px;background:radial-gradient(circle at 62% 48%,#f2f2f2 0,#cfcfcf 26%,rgba(60,60,60,.6) 38%,rgba(0,0,0,0) 60%),linear-gradient(0deg,#000 0,#0a0a0a 30%,rgba(0,0,0,0) 100%)}
.rules--ball{top:91px}
.rules--ball li{margin-bottom:10px}

.footnote-green{position:absolute;left:0;right:0;top:153px;text-align:center;font-style:italic;font-size:9px;color:var(--green)}
.call-banner{position:absolute;left:12px;right:20px;top:169px;height:61px;border-radius:6px;background:var(--green-light);color:var(--white);font-style:italic;font-weight:800;font-size:31px;line-height:28px;padding:3px 0 0 12px}
.call-banner span{display:block;text-align:right;padding-right:6px}

.footnote-white{position:absolute;left:0;right:0;top:162px;text-align:center;font-style:italic;font-size:9.5px}

.declare{position:absolute;left:44px;top:116px;font-weight:800;font-size:15px}
.declare sup{font-size:7px;vertical-align:7px}
.golfer-art{position:absolute;right:0;bottom:0;width:210px;height:172px;background:linear-gradient(180deg,rgba(255,255,255,0) 0%,#cfcfcf 45%,#1a1a1a 100%)}
.footer-bar{position:absolute;left:0;right:0;bottom:0;height:14px;background:#000}

.series{position:absolute;top:320px;font-weight:700;font-size:19.5px;color:var(--white);white-space:nowrap;letter-spacing:.2px}
.series--left{left:32px} .series--mid{left:415px} .series--right{left:801px}
</style>
</head>
<body>

<section class="panel panel--light panel--roulette">
  <h2 class="title"><span class="num num--red">1</span>TorBLIVVO<sup>TM</sup> ROULETTE</h2>
  <p class="tagline" style="top:52px">Every hole. Every shot. Everyone's watching.</p>
  <ol class="rules" style="top:87px">
    <li><span class="badge badge--red">1</span><span>Shuffle the <b>4 Ball Cards</b> (Curler, Snap, Sidewinder, TorBLIVVO™).</span></li>
    <li><span class="badge badge--red">2</span><span>Each player draws one card at the first tee (<b>your disaster</b> for the round).</span></li>
    <li><span class="badge badge--red">3</span><span>Hit YOUR disaster? Pay 1 point/$1 to the pot.</span></li>
    <li><span class="badge badge--red">4</span><span>Someone else hits your disaster? They pay YOU!</span></li>
  </ol>
  <p class="win">Win Condition: <b>Most points (or most $) at the end of 18 holes wins.</b></p>
  <div class="cards">
    <div class="mini-card mini-card--curl" role="img" aria-label="The Curler card art: golf ball on red"></div>
    <div class="mini-card mini-card--side" role="img" aria-label="The Sidewinder card art: speeding golf ball on green"></div>
    <div class="mini-card mini-card--snap" role="img" aria-label="The Snap card art: golf ball on blue"></div>
    <div class="mini-card mini-card--chucka" role="img" aria-label="TorBLIVVO card art: golf ball in dark grass"></div>
  </div>
</section>

<section class="panel panel--light panel--horsemen">
  <div class="horsemen-art" role="img" aria-label="Faint illustration of four hooded riders on horseback"></div>
  <h2 class="title"><span class="num num--blue">3</span>THE FOUR HORSEMEN</h2>
  <p class="tagline" style="top:66px">Every round has them. Collect them all.</p>
  <ul class="tally">
    <li><svg class="tick" viewBox="0 0 16 16"><circle cx="8" cy="8" r="8" fill="#d7141a"/><path d="M4 8.3l2.6 2.6L12 5.4" stroke="#fff" stroke-width="2" fill="none"/></svg><span class="name name--red">THE CURLER<sup>TM</sup></span><span class="pts">1 POINT</span></li>
    <li><svg class="tick" viewBox="0 0 16 16"><circle cx="8" cy="8" r="8" fill="#2e7d3a"/><path d="M4 8.3l2.6 2.6L12 5.4" stroke="#fff" stroke-width="2" fill="none"/></svg><span class="name name--green">THE SIDEWINDER<sup>TM</sup></span><span class="pts">1 POINT</span></li>
    <li><svg class="tick" viewBox="0 0 16 16"><circle cx="8" cy="8" r="8" fill="#22468a"/><path d="M4 8.3l2.6 2.6L12 5.4" stroke="#fff" stroke-width="2" fill="none"/></svg><span class="name name--blue">THE SNAP<sup>TM</sup></span><span class="pts">1 POINT</span></li>
    <li><svg class="tick" viewBox="0 0 16 16"><circle cx="8" cy="8" r="8" fill="#111"/><path d="M4 8.3l2.6 2.6L12 5.4" stroke="#fff" stroke-width="2" fill="none"/></svg><span class="name">TorBLIVVO<sup>TM</sup></span><span class="pts">1 POINT</span></li>
  </ul>
  <p class="sum">Add up points at 18 holes. Lowest score wins.</p>
  <div class="grand">
    <svg width="24" height="32" viewBox="0 0 24 32"><path d="M5 2h14v8a7 7 0 0 1-14 0z" fill="none" stroke="#fff" stroke-width="2"/><path d="M5 5H1v3a4 4 0 0 0 4 4M19 5h4v3a4 4 0 0 1-4 4" fill="none" stroke="#fff" stroke-width="1.6"/><path d="M12 17v8M6 30h12" stroke="#fff" stroke-width="2"/></svg>
    <div><h3>Grand TorBLIVVO™</h3><p>Hit all 4 in one round,<br>Everyone buys YOU a drink at the 19th hole!</p></div>
  </div>
</section>

<section class="panel panel--dark panel--ball">
  <div class="ball-art" role="img" aria-label="Golf ball marked TorBLIVVO resting in dark grass"></div>
  <h2 class="title"><span class="num num--white">5</span>THE TorBLIVVO<sup>TM</sup> BALL</h2>
  <p class="tagline" style="top:52px">One Ball to rule them all.</p>
  <ol class="rules rules--ball">
    <li><span class="badge badge--light">1</span><span>The TorBLIVVO Ball starts with Player #1.</span></li>
    <li><span class="badge badge--light">2</span><span>Make PAR or better? Pass the ball to another player.</span></li>
    <li><span class="badge badge--light">3</span><span>Bogey or worse? You keep it.</span></li>
    <li><span class="badge badge--light">4</span><span>Lose the <b>TorBLIVVO™ BALL</b>?<br><b>YOU BUY THE FIRST ROUND</b><br>at the clubhouse.</span></li>
  </ol>
</section>

<p class="series series--left">AMATEUR PERFORMANCE SERIES 2026</p>
<p class="series series--mid">HONEST PERFORMANCE TECHNOLOGY</p>
<p class="series series--right">BECAUSE IT'S DEFINITELY NOT YOUR SWING</p>

<section class="panel panel--light panel--calling">
  <h2 class="title"><span class="num num--green">2</span>CALL YOUR TorBLIVVO<sup>TM</sup></h2>
  <p class="tagline" style="top:46px">Think he can pull it off?</p>
  <ol class="rules" style="top:73px">
    <li><span class="badge badge--green">1</span><span>Before a player's shot, call out: "I'M CALLING TorBLIVVO!"</span></li>
    <li><span class="badge badge--green">2</span><span>If the shot ends in deep trouble (lost ball, unplayable, penalty area, or any spectacular TorBLIVVO™), the golfer owes the caller $1.</span></li>
    <li><span class="badge badge--green">3</span><span>If the golfer pulls off the shot, the caller owes HIM $1.</span></li>
  </ol>
  <p class="footnote-green">High risk. High reward, Maximum fun.</p>
  <div class="call-banner">I'M CALLING<span>TorBLIVVO!</span></div>
</section>

<section class="panel panel--dark panel--insurance">
  <h2 class="title"><span class="num num--white">4</span>TorBLIVVO<sup>TM</sup> INSURANCE</h2>
  <p class="tagline" style="top:46px">Because courage deserves a reward.</p>
  <ol class="rules" style="top:80px">
    <li><span class="badge badge--light">1</span><span>Before teeing off, say "<b>INSURANCE</b>" and put $1 in the pot.</span></li>
    <li><span class="badge badge--light">2</span><span>Hit woods/rough/disaster? <b>The pot pays you $5.</b></span></li>
    <li><span class="badge badge--light">3</span><span>Hit the fairway? Your $1 stays in the pot.</span></li>
  </ol>
  <p class="footnote-white">Play it safe. Or take the insurance.</p>
</section>

<section class="panel panel--light panel--bachelor">
  <div class="golfer-art" role="img" aria-label="Golfer mid-swing in front of dark pine tree silhouettes"></div>
  <div class="footer-bar"></div>
  <h2 class="title title--tight"><span class="num num--red">6</span>GROOM'S <span class="accent-red">LAST STAND</span><sup>TM</sup></h2>
  <p class="tagline" style="top:47px">The groom gets one free pass</p>
  <ol class="rules" style="top:73px">
    <li><span class="badge badge--red">1</span><span>The groom gets ONE TorBLIVVO™ PARDON per 9 holes.</span></li>
    <li><span class="badge badge--red">2</span><span>When he hits a truly awful shot, he can declare:</span></li>
  </ol>
  <p class="declare">"TORBLIVVO<sup>TM</sup>!</p>
  <ol class="rules" style="top:146px;right:205px">
    <li><span class="badge badge--red">3</span><span>Free replacement ball;<br>other 3 players pick<br>WHERE he plays it from.</span></li>
  </ol>
</section>

</body>
</html>
```